modern, IT themed business card for IT accelerator

Design a business card for tech oriented business accelerator. Prevailing color shall be orange.
we are operating in emerging markets and our mission is to provide co-working space, mentorship/coaching and ultimately seed financing IT startups.
also, we are helping financed ITs in obtaining next round financing, and to this end we are meeting with non IT/finance people and investment professionals..
that means card shall be designed to "impress" not only IT people (mostly liberal) but finance (more conservative)

Industry/Entity Type

Investment

Contact Information for Business Card

Company Name: Orin Venture Yard
Name: Levan Kutateli
Position: Partner
Address: 14, Marjanishvili Ave., Tbilisi 0112, Georgia
Tel: +995599348817
Email: l.kutateli@orinyard.ge
Website: www.orinyard.ge

Font styles to use
Sans Serif

Requirements
Must have
• Attached are logos of the company (portrait & landscape) choose any
Nice to have
• industry is IT and finance (in fact, financing IT startups). therefore design might have IT theme (inspiration from web or software designs)

```html
<!DOCTYPE html>
<html lang="en">
<head>
<meta charset="utf-8">
<title>Orin Venture Yard — Business Card</title>
<link href="https://fonts.googleapis.com/css2?family=Fira+Sans:ital,wght@0,400;0,600;1,400&display=swap" rel="stylesheet">
<style>
  :root {
    --backdrop: #ebebeb;
    --card-white: #fbfbfa;
    --orange-light: #dba570;
    --orange-deep: #c9782e;
    --accent: #e0a156;
    --grey: #8c8c8c;
    --grey-dark: #7a7a7a;
  }
  * { margin: 0; padding: 0; box-sizing: border-box; }
  html, body { width: 1200px; height: 720px; overflow: hidden; }
  body {
    background: var(--backdrop);
    font-family: "Fira Sans", sans-serif;
    position: relative;
  }
  .card {
    position: absolute;
    top: 205px;
    width: 525px;
    height: 300px;
    border-radius: 2px;
    box-shadow: 0 10px 24px rgba(0,0,0,0.12);
  }
  .card--front { left: 50px; background: var(--card-white); }
  .card--back {
    left: 625px;
    background: linear-gradient(160deg, var(--orange-light) 0%, var(--orange-deep) 100%);
    display: flex; flex-direction: column; align-items: center; justify-content: center; gap: 14px;
  }
  .brand {
    position: absolute;
    left: 28px; top: 62px;
    width: 180px;
    display: flex; flex-direction: column; align-items: center; gap: 16px;
  }
  .brand-dot {
    width: 92px; height: 92px; border-radius: 50%;
    border: 3px solid var(--grey);
    background: #fff;
  }
  .card--back .brand-dot { width: 120px; height: 120px; }
  .brand-name {
    color: var(--grey-dark);
    font-weight: 600;
    font-size: 22px;
    line-height: 1.1;
    text-align: center;
  }
  .card--back .brand-name { font-size: 28px; }
  .details {
    position: absolute;
    left: 235px; top: 34px;
  }
  .person-name {
    color: var(--accent);
    font-weight: 600;
    font-size: 25px;
    letter-spacing: 0.5px;
    text-transform: uppercase;
  }
  .person-title {
    color: var(--grey);
    font-style: italic;
    font-size: 16px;
    margin-top: 2px;
  }
  .address {
    color: var(--accent);
    font-size: 16px;
    line-height: 1.4;
    margin-top: 24px;
    font-style: normal;
  }
  .contacts { list-style: none; margin-top: 20px; }
  .contacts li {
    display: flex; align-items: center; gap: 7px;
    color: var(--grey);
    font-size: 15.5px;
    line-height: 1.65;
  }
  .contacts svg { width: 13px; height: 13px; flex: none; }
  .sep { color: var(--grey); }
</style>
</head>
<body>

  <section class="card card--front">
    <div class="brand">
      <div class="brand-dot"></div>
      <div class="brand-name">Orin Venture Yard</div>
    </div>
    <div class="details">
      <h1 class="person-name">Levan Kutateli</h1>
      <p class="person-title">Partner</p>
      <address class="address">14, Marjanishvili Ave,<br>Tbilisi 0112,<br>Georgia</address>
      <ul class="contacts">
        <li>
          <svg viewBox="0 0 16 16"><circle cx="8" cy="8" r="7" fill="none" stroke="#e0a156" stroke-width="1.6"/><path d="M5.5 4.5l1.5 0 .6 2-1 .8a5 5 0 0 0 2.1 2.1l.8-1 2 .6v1.5c-3.5.3-6.3-2.5-6-6z" fill="#e0a156"/></svg>
          <span class="sep">|</span> +995599348817
        </li>
        <li>
          <svg viewBox="0 0 16 16"><rect x="1" y="3" width="14" height="10" fill="#e0a156"/><path d="M1 3l7 6 7-6" fill="none" stroke="#fbfbfa" stroke-width="1.4"/></svg>
          <span class="sep">|</span> l.kutateli@orinyard.ge
        </li>
        <li>
          <svg viewBox="0 0 16 16"><circle cx="8" cy="8" r="6.5" fill="none" stroke="#e0a156" stroke-width="1.6"/><ellipse cx="8" cy="8" rx="2.8" ry="6.5" fill="none" stroke="#e0a156" stroke-width="1.2"/><path d="M1.5 8h13" stroke="#e0a156" stroke-width="1.2"/></svg>
          <span class="sep">|</span> www.orinyard.ge
        </li>
      </ul>
    </div>
  </section>

  <section class="card card--back">
    <div class="brand-dot"></div>
    <div class="brand-name">Orin Venture Yard</div>
  </section>

</body>
</html>
```